zVerda Corporate Website

zVerda is a well-funded start up developing an Online Marketing Platform for small businesses in Europe.
We are launching in February 2012 with all-in-one online marketing services including professional website, DIY SEO, Dashboard with Reports and Online marketing tools, and Support.
Our internal web designer has come up with a preliminary website design which we wish to continue to improve using new ideas, colours, layout, image, etc.
The brief is very simple - improve the website whether it is look & feel, ease of use, conversion rate - we are looking for overall improvements.
The contest will last 5 days and we will award the winner £300.
If you are the winner , you will also be required to provide designs for 3 more internal pages adhering to the proposed home page design.
Judging criteria : -
Visual Design
Layout must adhere to best practices and wire frame. If you decide to move elements around significantly please provide reason
Functional, informative and drives calls to action
Industry/Entity Type
Marketing
Look and feel
Each slider illustrates characteristics of the customer's brand and the style your logo design should communicate.

```html
<!DOCTYPE html>
<html lang="en">
<head>
<meta charset="utf-8">
<title>zVerda — Online Marketing for Small Business</title>
<link href="https://fonts.googleapis.com/css2?family=Open+Sans:wght@300;400;600;700&family=Oswald:wght@500;700&family=Arimo:wght@400;700&display=swap" rel="stylesheet">
<style>
:root{
  --green:#6aae1c;
  --green-dark:#4f8b0f;
  --green-light:#8cc63f;
  --orange:#f7941d;
  --orange-light:#fbb040;
  --red:#d7142b;
  --pink:#e5185a;
  --blue:#1b75d6;
  --ink:#333;
  --muted:#666;
  --page:#f4f4f2;
  --panel:#ebece7;
  --dark:#3b3b3b;
  --footer:#e6e6e4;
}
*{margin:0;padding:0;box-sizing:border-box}
html,body{width:778px;height:1200px;overflow:hidden}
body{position:relative;background:var(--page);font-family:"Arimo",Arial,sans-serif;color:var(--ink)}
.abs{position:absolute}

/* navigation */
.topbar{left:0;top:0;width:778px;height:32px;background:linear-gradient(#7cc12a,var(--green))}
.nav{left:112px;top:8px;display:flex;align-items:center;font:600 8.5px "Open Sans",sans-serif;color:#fff}
.nav a{color:#fff;text-decoration:none;padding:3px 6px}
.nav .sep{padding:0 3px;opacity:.9}
.nav .current{background:var(--orange);border-radius:3px}
.search{left:506px;top:5px;width:168px;height:21px;background:#fff;border:1px solid #d8e8c4}
.search svg{position:absolute;right:6px;top:3px}

/* hero */
.brand{left:110px;top:60px}
.brand .name{font:400 40px "Open Sans",sans-serif;color:#222;letter-spacing:-.5px}
.tagline{left:136px;top:133px;width:220px;font:300 15.5px/19px "Open Sans",sans-serif;color:var(--orange)}
.features{left:192px;top:182px;list-style:none;font:300 13px "Open Sans",sans-serif;color:#444}
.features li{height:22px;display:flex;align-items:center;gap:10px}
.cta{left:187px;top:286px;width:143px;height:50px;border-radius:6px;background:linear-gradient(#fbb040,#f57f17);color:#fff;text-align:center;box-shadow:0 6px 8px -4px rgba(0,0,0,.25)}
.cta .small{font:400 12px "Open Sans",sans-serif;margin-top:5px}
.cta .big{font:700 22px "Open Sans",sans-serif;line-height:24px}
.cta .go{position:absolute;right:-8px;bottom:-6px;width:24px;height:24px;border-radius:50%;background:#fff;box-shadow:0 1px 3px rgba(0,0,0,.3)}
.hero-art{left:376px;top:66px;width:304px;height:286px;border-radius:6px;background:radial-gradient(circle at 58% 55%,#d9d5cf 0,#e9ebe8 45%,rgba(244,244,242,0) 72%)}

/* offers */
.offers{left:98px;top:370px;width:583px;height:126px;background:var(--panel);border:1px solid #dfe0da}
.offer{top:19px;width:135px;height:89px;border-radius:3px;color:#fff;overflow:hidden;box-shadow:0 2px 3px rgba(0,0,0,.2)}
.offer .t1{position:absolute;left:9px;top:8px;font:700 18px "Oswald",sans-serif;line-height:20px}
.offer .t2{position:absolute;left:9px;top:28px;font:700 20px "Oswald",sans-serif;line-height:22px}
.offer .foot{position:absolute;left:0;bottom:6px;width:100%;text-align:center;font:400 8px "Arimo",sans-serif;line-height:10px;white-space:nowrap}
.offer .tag{position:absolute;right:-22px;top:12px;width:90px;height:14px;transform:rotate(45deg);background:#fff;color:var(--red);font:700 8px/14px "Arimo",sans-serif;text-align:center}
.offer.setup{left:5px;background:linear-gradient(#e8212e,#b3121f)}
.offer.pro{left:149px;background:linear-gradient(#f6a21b,#e26b10)}
.offer.turbo{left:292px;background:linear-gradient(#5fb22c,#2e7d12)}
.how{left:445px;top:22px;width:128px}
.how h3{font:400 12.5px "Open Sans",sans-serif;color:var(--pink);margin-bottom:8px}
.how p{font:400 7px/11px "Arimo",sans-serif;color:#444;text-align:justify}

/* ribbon */
.ribbon-tail{top:504px}
.ribbon{left:90px;top:496px;width:598px;height:78px;background:linear-gradient(#78bd2a,var(--green));border-top:2px dashed rgba(255,255,255,.35);text-align:center;color:#fff}
.ribbon h2{font:300 18.5px "Open Sans",sans-serif;margin-top:18px}
.ribbon h2 b{font-weight:400}
.ribbon p{font:300 13.5px "Open Sans",sans-serif;margin-top:1px}

/* about */
.about-title{left:109px;top:592px;font:300 18px "Open Sans",sans-serif;color:#222}
.about{left:109px;top:620px;width:274px;font:400 7px/11px "Arimo",sans-serif;color:#444;text-align:justify}
.about p{text-indent:22px;margin-bottom:11px}
.about em{font-style:normal;color:var(--orange)}
.callus{left:395px;top:622px;width:280px;height:42px;background:var(--dark);border-radius:2px;color:#fff}
.callus .ico{position:absolute;left:3px;top:3px;width:36px;height:36px;background:#555;border-radius:2px}
.callus .txt{position:absolute;left:55px;top:10px;font:700 15px "Open Sans",sans-serif;white-space:nowrap}
.callus .txt span{color:#fbc40a;font-size:22px;margin-left:6px;position:relative;top:1px}
.card{width:134px;height:60px;background:#fafafa;border:1px solid #cfcfcf;border-radius:2px}
.card h4{height:15px;text-align:center;color:#fff;font:400 10.5px/15px "Open Sans",sans-serif}
.card p{position:absolute;left:36px;top:26px;width:92px;font:400 7px/9px "Arimo",sans-serif;color:#555}
.card svg{position:absolute;left:7px;top:24px}
.c-orange h4{background:var(--orange)}
.c-green h4{background:var(--green)}
.c-blue h4{background:var(--blue)}
.c-pink h4{background:var(--pink)}

/* examples */
.ex-title{left:122px;top:866px;font:400 11px/14px "Open Sans",sans-serif;color:var(--green)}
.ex-text{left:122px;top:901px;width:130px;font:400 7px/11px "Arimo",sans-serif;color:#777}
.more{left:202px;top:967px;font:400 7px "Arimo",sans-serif;color:var(--orange);display:flex;align-items:center;gap:4px}
.shot{background:linear-gradient(#3a3f4a,#e9ecef 30%,#f7f7f7)}
.shot.side{top:863px;height:108px}
.shot.main{left:366px;top:858px;width:199px;height:118px;border:3px solid var(--green)}

/* footer */
.footer{left:0;top:1010px;width:778px;height:190px;background:var(--footer);border-top:2px solid var(--green)}
.f-brand{left:96px;top:1012px;width:106px;height:46px;background:var(--green);display:flex;align-items:center;justify-content:center}
.f-brand .name{font:400 21px "Open Sans",sans-serif;color:#222}
.follow{left:107px;top:1072px;font:400 11.5px "Open Sans",sans-serif;color:#333}
.social{top:1093px;width:17px;height:17px;border-radius:50%;background:#fff;border:1px solid #d5d5d5}
.col-head{top:1038px;display:flex;align-items:center;gap:7px;font:400 12px "Open Sans",sans-serif;color:#333;white-space:nowrap}
.links{top:1071px;list-style:none;font:400 7.2px "Arimo",sans-serif;color:#666;white-space:nowrap}
.links li{height:18px;display:flex;align-items:center;gap:5px}
.links li::before{content:"";border-left:3px solid var(--orange);border-top:2px solid transparent;border-bottom:2px solid transparent}
.email{left:578px;top:1072px;width:78px;height:15px;background:#fff;border:1px solid #ddd;font:italic 6.5px/13px "Arimo",sans-serif;color:#aaa;padding-left:4px}
.plus{left:659px;top:1072px;width:17px;height:15px;background:var(--blue);border-radius:2px}
.like{left:580px;top:1094px;display:flex;gap:3px;font:400 6.5px "Arimo",sans-serif}
.like span{border:1px solid #bbb;background:#fff;padding:1px 3px;color:#3b5998}
.like span+span{color:#333}
.copy{left:0;top:1165px;width:778px;text-align:center;font:400 7px "Arimo",sans-serif;color:#555}
</style>
</head>
<body>

<div class="abs topbar"></div>
<nav class="abs nav">
  <a class="current">HOME</a><span class="sep">I</span>
  <a>ABOUT US</a><span class="sep">I</span>
  <a>QUICK TOUR</a><span class="sep">I</span>
  <a>PRICING</a><span class="sep">I</span>
  <a>CONTACT US</a><span class="sep">I</span>
  <a>LOGIN</a>
</nav>
<div class="abs search">
  <svg width="16" height="14" viewBox="0 0 16 14"><circle cx="6" cy="6" r="4.5" fill="none" stroke="#f39c12" stroke-width="2"/><line x1="9.5" y1="9" x2="14.5" y2="13" stroke="#f39c12" stroke-width="2.5" stroke-linecap="round"/></svg>
</div>

<div class="abs brand"><span class="name">zVerda</span></div>
<p class="abs tagline">Getting a website has never been so simple</p>
<ul class="abs features">
  <li><svg width="12" height="10" viewBox="0 0 12 10"><path d="M1 5l3.5 3.5L11 1" fill="none" stroke="#6aae1c" stroke-width="2.4"/></svg>Business Websites</li>
  <li><svg width="12" height="10" viewBox="0 0 12 10"><path d="M1 5l3.5 3.5L11 1" fill="none" stroke="#6aae1c" stroke-width="2.4"/></svg>Online Marketing</li>
  <li><svg width="12" height="10" viewBox="0 0 12 10"><path d="M1 5l3.5 3.5L11 1" fill="none" stroke="#6aae1c" stroke-width="2.4"/></svg>Dashboard Controls</li>
  <li><svg width="12" height="10" viewBox="0 0 12 10"><path d="M1 5l3.5 3.5L11 1" fill="none" stroke="#6aae1c" stroke-width="2.4"/></svg>Full Setup &amp; Support</li>
</ul>
<a class="abs cta">
  <div class="small">Sign up NOW for</div>
  <div class="big">FREE!</div>
  <span class="go"><svg width="24" height="24" viewBox="0 0 24 24"><path d="M6 10h7V6l6 6-6 6v-4H6z" fill="#4caf1c"/></svg></span>
</a>
<div class="abs hero-art" role="img" aria-label="Photo of a thoughtful businessman surrounded by speech bubbles naming marketing services: PPC, SEO, hosting, web design, email marketing, reporting and more"></div>

<section class="abs offers">
  <div class="abs offer setup"><div class="t1">Free</div><div class="t2">SETUP</div><div class="tag">£199 Value</div><div class="foot" style="font-size:11px;line-height:12px">WEB OFFER ONLY</div></div>
  <div class="abs offer pro"><div class="t1">Pro</div><div class="t2">PACKAGE</div><div class="tag">£22 / month</div><div class="foot">Bussiness Website &amp; Easy Dashboard</div></div>
  <div class="abs offer turbo"><div class="t1" style="font-size:15px">TURBO SALES</div><div class="t2" style="top:26px;font-size:15px">PRO PLUS</div><div class="tag">£29 / month</div><div class="foot" style="font-size:9px;line-height:11px">Business Website,<br>Easy Dashboard &amp; ppc Sales</div></div>
  <div class="abs how">
    <h3>How does it work?</h3>
    <p>Neque porro quisquam est qui dolorem ipsum quia dolor vel eum iriure dolor in hendrerit in vulputate velit dou site vesse molestie consequat, vel illumst amet, adipisci velit"</p>
  </div>
</section>

<svg class="abs ribbon-tail" style="left:42px" width="60" height="72" viewBox="0 0 60 72"><path d="M0 0H60V72H0L22 36Z" fill="#5a9a16"/></svg>
<svg class="abs ribbon-tail" style="left:676px" width="60" height="72" viewBox="0 0 60 72"><path d="M60 0H0V72H60L38 36Z" fill="#5a9a16"/></svg>
<div class="abs ribbon">
  <h2>The Complete Online Marketing Solution for <b>Small Business Websites</b></h2>
  <p>“Get a big online presence and more sales leads in 30 minutes”</p>
</div>

<h2 class="abs about-title">About Us</h2>
<div class="abs about">
  <p><em>zVerda</em> will build your business website, optimise SEO marketing and make recommendations on best practices to help you win customers. Let our team of experts design a business website for you. Choose a business website from <em>zVerda's</em> broad array of fabulous, customisable business websites and our experts will have your business online in minutes. <em>zVerda</em> lets you create a professional business website without the need to know how to code or programme.</p>
  <p>Your business website comes with automatic Internet marketing, marketing on the Internet is easy with <em>zVerda</em>, we automatically optimise your site for SEO marketing and we can run search ad campaigns when you need them. Get a business website with online marketing now. <em>zVerda</em> brings your Small Business Website to LIFE!</p>
  <p>View our example business websites above, watch the video demo to see how to make a business website or call us now and get your business marketing online today. The <em>zVerda</em> website builder gives you a professional online appearance - post your own images, give customers your latest news and create customer testimonials, it's the most complete online marketing solution for your business.</p>
</div>

<div class="abs callus">
  <div class="ico"><svg width="36" height="36" viewBox="0 0 36 36"><path d="M12 8c2-1 4 0 4 2l1 4c0 1-1 2-2 2 1 3 2 5 4 6 1-1 2-1 3 0l3 2c1 1 1 3-1 4-4 2-9-1-12-7-3-5-3-11 0-13z" fill="#ddd"/></svg></div>
  <div class="txt">CALL US<span>800-555-0199</span></div>
</div>

<div class="abs card c-orange" style="left:395px;top:674px"><h4>Case Studies</h4>
  <svg width="24" height="22" viewBox="0 0 24 22"><rect x="1" y="4" width="4" height="16" fill="#777"/><rect x="7" y="10" width="4" height="10" fill="#999"/><rect x="13" y="13" width="4" height="7" fill="#777"/><rect x="0" y="20" width="24" height="2" fill="#555"/></svg>
  <p>Read real stories about small businesses online</p></div>
<div class="abs card c-green" style="left:542px;top:674px"><h4>How to</h4>
  <svg width="20" height="26" viewBox="0 0 20 26"><circle cx="10" cy="9" r="7.5" fill="none" stroke="#888" stroke-width="1.5"/><rect x="7" y="17" width="6" height="6" fill="#888"/></svg>
  <p>Learn from our online marketing tips for small business</p></div>
<div class="abs card c-blue" style="left:395px;top:748px"><h4>News &amp; Chatter</h4>
  <svg width="26" height="24" viewBox="0 0 26 24"><path d="M2 2h16v11H8l-5 4v-4H2z" fill="#777"/><path d="M20 7h4v10h-1v4l-4-4h-8v-2h9z" fill="#999"/></svg>
  <p>Get up-to-date news and chatter about online marketing</p></div>
<div class="abs card c-pink" style="left:542px;top:748px"><h4>Demo</h4>
  <svg width="26" height="26" viewBox="0 0 26 26"><circle cx="13" cy="14" r="11" fill="#888"/><path d="M13 7v7h5" stroke="#fff" stroke-width="2" fill="none"/></svg>
  <p>Find out what zVerda can do for your business.</p></div>

<h3 class="abs ex-title">View examples of our<br>stunning business websites</h3>
<p class="abs ex-text">Duis autem vel eum iriure dolor in hendrerit in vulputate velit esse molestie consequat, vel illum dolore eu feugiat nulla facilisis at vero eros et accumsan esse molestie.</p>
<a class="abs more"><svg width="8" height="8" viewBox="0 0 8 8"><circle cx="4" cy="4" r="3.5" fill="#fff" stroke="#999" stroke-width=".8"/><path d="M3 2.3l2 1.7-2 1.7z" fill="#f7941d"/></svg>View more</a>
<svg class="abs" style="left:292px;top:896px" width="14" height="26" viewBox="0 0 14 26"><path d="M14 0L0 13l14 13z" fill="#8a8a8a"/></svg>
<svg class="abs" style="left:630px;top:896px" width="14" height="26" viewBox="0 0 14 26"><path d="M0 0l14 13L0 26z" fill="#8cc63f"/></svg>
<div class="abs shot side" style="left:324px;width:50px" role="img" aria-label="Screenshot of an example business website"></div>
<div class="abs shot side" style="left:560px;width:56px;background:linear-gradient(#1e2a4a,#2f5fbf 60%,#e8edf5)" role="img" aria-label="Screenshot of an example business website"></div>
<div class="abs shot main" role="img" aria-label="Screenshot of a featured example business website"></div>

<footer class="abs footer"></footer>
<div class="abs f-brand"><span class="name">zVerda</span></div>
<p class="abs follow">Follow</p>
<span class="abs social" style="left:109px"></span>
<span class="abs social" style="left:138px"></span>
<span class="abs social" style="left:169px"></span>

<div class="abs col-head" style="left:214px">
  <svg width="20" height="20" viewBox="0 0 20 20"><circle cx="10" cy="10" r="6.5" fill="none" stroke="#777" stroke-width="3" stroke-dasharray="3 2"/><circle cx="10" cy="10" r="3" fill="#777"/></svg>OurServices</div>
<ul class="abs links" style="left:214px"><li>Search Engine Optimation (SEO)</li><li>Social Media</li><li>Web Analytics</li></ul>

<div class="abs col-head" style="left:362px">
  <svg width="18" height="22" viewBox="0 0 18 22"><rect x="1" y="1" width="16" height="20" rx="2" fill="#777"/><rect x="4" y="4" width="10" height="13" fill="#eee"/></svg>ContactUs</div>
<ul class="abs links" style="left:358px"><li>Contact Us</li><li>Customer Support</li><li>Request a call back</li><li>FAQ's</li></ul>

<div class="abs col-head" style="left:468px">
  <svg width="28" height="20" viewBox="0 0 28 20"><path d="M1 2h9l2 2h13v15H1z" fill="#777"/><path d="M4 8h23l-3 11H1z" fill="#999"/></svg>Navigation</div>
<ul class="abs links" style="left:467px"><li>Site Map</li><li>Terms and Condition</li><li>Privacy &amp; Policy</li><li>Get in Touch</li></ul>

<div class="abs col-head" style="left:578px">
  <svg width="28" height="20" viewBox="0 0 28 20"><rect x="1" y="2" width="26" height="16" fill="#888"/><path d="M1 2l13 10L27 2" fill="none" stroke="#eee" stroke-width="1.5"/></svg>Subscribe</div>
<div class="abs email">Type your email here</div>
<div class="abs plus"><svg width="17" height="15" viewBox="0 0 17 15"><path d="M8.5 3v9M4 7.5h9" stroke="#fff" stroke-width="2.4"/></svg></div>
<div class="abs like"><span>Like</span><span>62</span></div>

<p class="abs copy">Copyright © 2011 zVerda Pvt. Ltd 2011 - &nbsp;All rights reserved. &nbsp;Managed by zVerda &nbsp; | &nbsp; Admin</p>

</body>
</html>
```